BRV Stationary
BRV All The Way!
Corporate
Dale Orwick
CEO
2380 Tallow St. Suite #240 San Francisco, CA 94107
dorwick@brvatw.com
brvatw.com
looking for a water mark on the business cards and stationary. Check out the brief for the logo for more ideas. http://orders.markcraftdepot.com/contests/bright-relay-ventures/readbrief

```html
<!DOCTYPE html>
<html lang="en">
<head>
<meta charset="utf-8">
<title>BRV Stationary – Business Cards</title>
<link rel="stylesheet" href="https://fonts.googleapis.com/css2?family=Roboto:wght@400;500;700;900&display=swap">
<style>
  :root {
    --bg: #e9e9e7;
    --blue: #3d5ea8;
    --blue-dark: #2f4b8c;
    --green: #5aa843;
    --white: #ffffff;
    --paper: #f6f6f6;
    --black: #111214;
    --black-soft: #24262a;
    --ink: #2a2a2a;
    --ink-light: #e4e4e4;
    --muted: #8a8a8a;
  }
  * { box-sizing: border-box; margin: 0; padding: 0; }
  html, body { width: 1200px; height: 914px; overflow: hidden; }
  body {
    background: var(--bg);
    font-family: "Roboto", Arial, sans-serif;
    color: var(--ink);
  }
  .sheet {
    width: 1200px; height: 914px;
    display: grid;
    grid-template-columns: 480px 480px;
    grid-template-rows: 280px 280px;
    gap: 70px 80px;
    justify-content: center;
    align-content: center;
  }
  .card {
    position: relative;
    width: 480px; height: 280px;
    border-radius: 12px;
    overflow: hidden;
    box-shadow: 0 6px 18px rgba(0,0,0,.18);
  }
  .card--light { background: linear-gradient(180deg, var(--white), var(--paper)); }
  .card--dark { background: linear-gradient(180deg, var(--black-soft), var(--black)); color: var(--ink-light); }

  .card__header {
    position: absolute; left: 0; top: 0; right: 0; height: 100px;
    background: linear-gradient(180deg, var(--blue), var(--blue-dark));
    border-bottom: 5px solid var(--green);
    padding: 26px 0 0 28px;
    color: var(--white);
  }
  .card__name { font-size: 25px; font-weight: 700; line-height: 1; }
  .card__title { font-size: 14px; margin-top: 4px; }
  .card__watermark {
    position: absolute; right: 30px; top: 18px;
    font-size: 62px; font-weight: 900; letter-spacing: 2px;
    color: rgba(255,255,255,.08);
  }

  .brand { display: flex; align-items: center; gap: 10px; }
  .brand__square { width: 20px; height: 20px; background: var(--green); }
  .brand__name { font-size: 58px; font-weight: 900; color: var(--blue); letter-spacing: 2px; line-height: 1; }
  .card--dark .brand__name { color: var(--blue); }

  .card__brand { position: absolute; left: 28px; top: 140px; }

  .contact {
    position: absolute; left: 250px; top: 136px;
    font-size: 11px; line-height: 15px;
  }
  .contact__address { margin-bottom: 4px; }
  .contact__row { display: flex; align-items: center; gap: 6px; }
  .contact__row svg { width: 10px; height: 10px; flex: none; }

  .card--back .card__brand {
    left: 50%; top: 96px; transform: translateX(-50%);
  }
  .card--back .brand__name { font-size: 70px; }
  .card__url {
    position: absolute; left: 0; right: 0; bottom: 34px;
    text-align: center; font-size: 11px; font-weight: 500; letter-spacing: 4px;
  }
</style>
</head>
<body>
<main class="sheet">

  <!-- Front, light -->
  <section class="card card--light card--front">
    <header class="card__header">
      <div class="card__name">Dale Orwick</div>
      <div class="card__title">CEO</div>
      <div class="card__watermark">BRV</div>
    </header>
    <div class="card__brand brand"><span class="brand__square"></span><span class="brand__name">BRV</span></div>
    <address class="contact" style="font-style:normal">
      <div class="contact__address">2380 Tallow St. Suite #240<br>San Francisco, CA 94107</div>
      <div class="contact__row"><svg viewBox="0 0 10 10"><circle cx="5" cy="5" r="5" fill="#3d5ea8"/><path d="M3 2.5h1.2l.5 1.5-.7.6a4 4 0 0 0 1.6 1.6l.6-.7 1.5.5V7.5A5 5 0 0 1 3 2.5z" fill="#fff"/></svg>415-555-0142</div>
      <div class="contact__row"><svg viewBox="0 0 10 10"><circle cx="5" cy="5" r="5" fill="#3d5ea8"/><rect x="2.5" y="3" width="5" height="4" fill="#fff"/></svg>415-555-0187</div>
      <div class="contact__row"><svg viewBox="0 0 10 10"><circle cx="5" cy="5" r="5" fill="#3d5ea8"/><path d="M2.5 3.3h5v3.4h-5zM2.5 3.3 5 5.2l2.5-1.9" fill="none" stroke="#fff" stroke-width=".8"/></svg>dorwick@brvatw.com</div>
    </address>
  </section>

  <!-- Front, dark -->
  <section class="card card--dark card--front">
    <header class="card__header">
      <div class="card__name">Dale Orwick</div>
      <div class="card__title">CEO</div>
      <div class="card__watermark">BRV</div>
    </header>
    <div class="card__brand brand"><span class="brand__square"></span><span class="brand__name">BRV</span></div>
    <address class="contact" style="font-style:normal">
      <div class="contact__address">2380 Tallow St. Suite #240<br>San Francisco, CA 94107</div>
      <div class="contact__row"><svg viewBox="0 0 10 10"><circle cx="5" cy="5" r="5" fill="#e4e4e4"/><path d="M3 2.5h1.2l.5 1.5-.7.6a4 4 0 0 0 1.6 1.6l.6-.7 1.5.5V7.5A5 5 0 0 1 3 2.5z" fill="#111"/></svg>415-555-0142</div>
      <div class="contact__row"><svg viewBox="0 0 10 10"><circle cx="5" cy="5" r="5" fill="#e4e4e4"/><rect x="2.5" y="3" width="5" height="4" fill="#111"/></svg>415-555-0187</div>
      <div class="contact__row"><svg viewBox="0 0 10 10"><circle cx="5" cy="5" r="5" fill="#e4e4e4"/><path d="M2.5 3.3h5v3.4h-5zM2.5 3.3 5 5.2l2.5-1.9" fill="none" stroke="#111" stroke-width=".8"/></svg>dorwick@brvatw.com</div>
    </address>
  </section>

  <!-- Back, light -->
  <section class="card card--light card--back">
    <div class="card__brand brand"><span class="brand__square"></span><span class="brand__name">BRV</span></div>
    <div class="card__url">www.brvatw.com</div>
  </section>

  <!-- Back, dark -->
  <section class="card card--dark card--back">
    <div class="card__brand brand"><span class="brand__square"></span><span class="brand__name">BRV</span></div>
    <div class="card__url">www.brvatw.com</div>
  </section>

</main>
</body>
</html>
```